Beauty website banner

We are an Australian beauty website selling mid and high end cosmetics and beauty products.

We need a banner that tells customers they can share their product wishlists with friends to let them know what they want for Christmas.

Target Market(s)

Female, 30-60, white collar

Industry/Entity Type

Cosmetics

Requirements
Must have
• 600 x 150 pixels in size

Words to be as follows, not including the (") of course.

"Share your wishlist with friends and family for Christmas!"

(Then in smaller font) "Just log in to your account, go to your wishlist and click on the ‘share wishlist’ button"

```html
<!DOCTYPE html>
<html lang="en">
<head>
<meta charset="UTF-8">
<title>Share Your Wishlist – Christmas Banner</title>
<link href="https://fonts.googleapis.com/css2?family=Righteous&family=Comfortaa:wght@400&display=swap" rel="stylesheet">
<style>
  :root {
    --bg-pink: #f5a7ee;
    --bg-pink-light: #f9c4f4;
    --portrait-skin: #e9d3d6;
    --portrait-shadow: #c9a7b6;
    --heading-red: #b0102a;
    --heading-red-dark: #6e0a1c;
    --heading-red-bright: #e8203a;
    --blob-coral: #f0645f;
    --blob-coral-soft: #f48a84;
    --note-ink: #7a0c18;
    --note-fill: #fde2ea;
  }
  * { margin: 0; padding: 0; box-sizing: border-box; }
  html, body {
    width: 1200px;
    height: 300px;
    overflow: hidden;
    background: var(--bg-pink);
  }
  .banner {
    position: relative;
    width: 1200px;
    height: 300px;
    overflow: hidden;
    background: linear-gradient(90deg, var(--bg-pink) 0%, var(--bg-pink-light) 55%, var(--bg-pink) 100%);
  }
  .banner__portrait {
    position: absolute;
    left: 0;
    top: 0;
    width: 440px;
    height: 300px;
    background:
      radial-gradient(ellipse 170px 220px at 150px 150px, var(--portrait-skin) 0%, var(--portrait-shadow) 55%, rgba(245,167,238,0) 100%);
  }
  .banner__headline {
    position: absolute;
    left: 380px;
    width: 800px;
    text-align: center;
    font-family: "Righteous", sans-serif;
    text-transform: uppercase;
    background: linear-gradient(180deg, var(--heading-red-bright) 0%, var(--heading-red) 55%, var(--heading-red-dark) 100%);
    -webkit-background-clip: text;
    background-clip: text;
    color: transparent;
  }
  .banner__headline--main {
    top: 38px;
    font-size: 25px;
    letter-spacing: 0.5px;
  }
  .banner__headline--season {
    top: 108px;
    left: 450px;
    width: 400px;
    font-size: 38px;
  }
  .banner__note-shape {
    position: absolute;
    left: 270px;
    top: 160px;
    width: 930px;
    height: 130px;
  }
  .banner__note {
    position: absolute;
    left: 300px;
    top: 184px;
    width: 880px;
    font-family: "Comfortaa", sans-serif;
    font-size: 25px;
    line-height: 42px;
    text-align: center;
    color: var(--note-fill);
    -webkit-text-stroke: 0.8px var(--note-ink);
  }
  .banner__note-line--first {
    display: block;
    padding-right: 220px;
  }
  .banner__note-line--second {
    display: block;
  }
</style>
</head>
<body>
  <div class="banner">
    <div class="banner__portrait" role="img" aria-label="Soft-focus beauty portrait of a woman with a beaded necklace, fading into the pink background"></div>

    <h1 class="banner__headline banner__headline--main">Share your wishlist with friends and family</h1>
    <h2 class="banner__headline banner__headline--season">For Christmas!</h2>

    <svg class="banner__note-shape" viewBox="0 0 930 130" aria-hidden="true">
      <defs>
        <filter id="soft-edge" x="-5%" y="-20%" width="110%" height="140%">
          <feGaussianBlur stdDeviation="3"/>
        </filter>
      </defs>
      <path fill="var(--blob-coral)" filter="url(#soft-edge)"
        d="M150 22 C190 6 560 4 600 14 C630 22 640 40 660 48 C720 52 880 46 912 62
           C930 80 925 108 900 118 C760 128 220 128 60 122 C20 120 8 102 14 86
           C22 64 80 62 130 58 C136 40 138 28 150 22 Z"/>
    </svg>

    <p class="banner__note">
      <span class="banner__note-line--first">Just log in to your account</span>
      <span class="banner__note-line--second">go to your wishlist and click on the ‘share wishlist’ button</span>
    </p>
  </div>
</body>
</html>
```